Create a Branded Four Stage Lifecycle Diagram

We need a rethink / redesign of our Lifecycle. We created it and have used it till now but it is not professional and needs our branding as well. We use it for presentations, for analysis with schools when we are consulting on site and it should look equally good on a powerpoint slide as on a handout and, of course, as a JPG that we can copy onto documents that we create. It does not have to look like what we currently have. I will include the article so you can see what we are trying to achieve. Eventually we want to be able to trademark it. It should include copyright 2020 Harbor Academy Advisors. Each stafe should reflect its characteristics in some fashion.

Target Market(s)

We serve K-12 Christian private schools

Industry/Entity Type

Education

Font styles to use
Sans Serif

Colors

Designer to choose colors to be used in the design.

Requirements
Must have
• HAA logo
• copyright notice
• title: HAA Lifecycle
Nice to have
• In the article, you will see the Corporate Lifecycle. It is completely different from ours. You will also see our current 'design'. It does not have to be like the one we currently have - it is not a refresh - it is a new design.
Should not have
• There must be no chance that our design could be confused with the corporate lifecycle.

```html
<!DOCTYPE html>
<html lang="en">
<head>
<meta charset="utf-8">
<title>The HAA Christian School Lifecycle</title>
<link rel="stylesheet" href="https://fonts.googleapis.com/css2?family=Source+Sans+3:wght@400;600&display=swap">
<style>
  :root {
    --bg: #ebebeb;
    --ink: #77787b;
    --rule: #7d7d7f;
    --brand: #1b6d9e;
    --disc: #f7f7f7;
    --purple-a: #2e3a92;
    --purple-b: #6f73b8;
    --blue-a: #0080c6;
    --blue-b: #00baf0;
    --green-a: #00ad4f;
    --green-b: #8ec94c;
    --red-a: #bd1e2d;
    --red-b: #ee3e2f;
    --arc-top: #0095da;
    --arc-left: #5b63ae;
    --arc-bottom: #3cb54a;
    --arc-right: #e0312e;
  }
  html, body { margin: 0; padding: 0; overflow: hidden; background: var(--bg); }
  .canvas {
    position: relative;
    width: 1200px;
    height: 857px;
    background: var(--bg);
    font-family: "Source Sans 3", sans-serif;
    color: var(--ink);
    overflow: hidden;
  }
  .brand-name {
    position: absolute;
    left: 84px;
    top: 88px;
    margin: 0;
    font-size: 62px;
    font-weight: 400;
    letter-spacing: 1px;
    color: var(--brand);
    line-height: 1;
  }
  .title-block {
    position: absolute;
    left: 671px;
    top: 78px;
    width: 488px;
    height: 64px;
    border-top: 1.5px solid var(--rule);
    border-bottom: 1.5px solid var(--rule);
    box-sizing: border-box;
  }
  .title {
    margin: 0;
    font-size: 33px;
    font-weight: 400;
    line-height: 60px;
    text-align: right;
    color: var(--ink);
    white-space: nowrap;
  }
  .diagram { position: absolute; left: 0; top: 0; }
  .stage-label { font-size: 23.5px; fill: var(--ink); }
  .stage-name { fill: #fff; font-weight: 400; }
  .copyright {
    position: absolute;
    left: 0;
    width: 1200px;
    top: 815px;
    margin: 0;
    text-align: center;
    font-size: 19px;
    color: var(--ink);
  }
</style>
</head>
<body>
<div class="canvas">
  <p class="brand-name">HAA</p>

  <div class="title-block">
    <h1 class="title">The HAA Christian School Lifecycle</h1>
  </div>

  <svg class="diagram" width="1200" height="857" viewBox="0 0 1200 857" aria-label="Four stage lifecycle diagram">
    <defs>
      <linearGradient id="grad-purple" x1="0" x2="1"><stop offset="0" stop-color="var(--purple-a)"/><stop offset="1" stop-color="var(--purple-b)"/></linearGradient>
      <linearGradient id="grad-blue" x1="0" x2="1"><stop offset="0" stop-color="var(--blue-a)"/><stop offset="1" stop-color="var(--blue-b)"/></linearGradient>
      <linearGradient id="grad-green" x1="0" x2="1"><stop offset="0" stop-color="var(--green-a)"/><stop offset="1" stop-color="var(--green-b)"/></linearGradient>
      <linearGradient id="grad-red" x1="0" x2="1"><stop offset="0" stop-color="var(--red-a)"/><stop offset="1" stop-color="var(--red-b)"/></linearGradient>
      <linearGradient id="rule-purple" x1="0" y1="0" x2="0" y2="1"><stop offset="0" stop-color="var(--purple-a)"/><stop offset="1" stop-color="var(--purple-b)"/></linearGradient>
      <linearGradient id="rule-blue" x1="0" y1="0" x2="0" y2="1"><stop offset="0" stop-color="var(--blue-a)"/><stop offset="1" stop-color="var(--blue-b)"/></linearGradient>
      <linearGradient id="rule-green" x1="0" y1="0" x2="0" y2="1"><stop offset="0" stop-color="var(--green-a)"/><stop offset="1" stop-color="var(--green-b)"/></linearGradient>
      <linearGradient id="rule-red" x1="0" y1="0" x2="0" y2="1"><stop offset="0" stop-color="var(--red-a)"/><stop offset="1" stop-color="var(--red-b)"/></linearGradient>
      <filter id="disc-shadow" x="-30%" y="-30%" width="160%" height="170%">
        <feDropShadow dx="3" dy="6" stdDeviation="7" flood-color="#000" flood-opacity="0.18"/>
      </filter>
      <filter id="arrow-shadow" x="-50%" y="-50%" width="200%" height="200%">
        <feDropShadow dx="3" dy="4" stdDeviation="3" flood-color="#000" flood-opacity="0.2"/>
      </filter>
    </defs>

    <!-- connecting arcs -->
    <g class="arcs" fill="none" stroke-width="3">
      <path d="M549 315 Q620 290 690 313" stroke="var(--arc-top)"/>
      <path d="M439 427 Q418 491 438 555" stroke="var(--arc-left)"/>
      <path d="M542 673 Q618 705 695 675" stroke="var(--arc-bottom)"/>
      <path d="M802 424 Q830 491 807 558" stroke="var(--arc-right)"/>
    </g>

    <!-- arrow heads -->
    <g class="arrows" filter="url(#arrow-shadow)">
      <polygon points="609,301 639,283 639,320" fill="var(--arc-top)"/>
      <polygon points="410,479 447,479 428,509" fill="var(--arc-left)"/>
      <polygon points="606,670 606,708 636,689" fill="var(--arc-bottom)"/>
      <polygon points="797,512 835,512 816,481" fill="var(--arc-right)"/>
    </g>

    <!-- stage discs -->
    <g class="stage">
      <circle cx="474" cy="352" r="82" fill="var(--disc)" filter="url(#disc-shadow)"/>
      <circle cx="474" cy="352" r="63.5" fill="url(#grad-purple)"/>
      <text class="stage-name" x="475" y="359" text-anchor="middle" font-size="18">Entrepreneurial</text>
    </g>
    <g class="stage">
      <circle cx="764" cy="352" r="82" fill="var(--disc)" filter="url(#disc-shadow)"/>
      <circle cx="764" cy="352" r="63.5" fill="url(#grad-blue)"/>
      <text class="stage-name" x="764" y="360" text-anchor="middle" font-size="22">Dying</text>
    </g>
    <g class="stage">
      <circle cx="474" cy="629" r="82" fill="var(--disc)" filter="url(#disc-shadow)"/>
      <circle cx="474" cy="629" r="63.5" fill="url(#grad-green)"/>
      <text class="stage-name" x="475" y="636" text-anchor="middle" font-size="20">Adolescent</text>
    </g>
    <g class="stage">
      <circle cx="764" cy="629" r="82" fill="var(--disc)" filter="url(#disc-shadow)"/>
      <circle cx="764" cy="629" r="63.5" fill="url(#grad-red)"/>
      <text class="stage-name" x="767" y="638" text-anchor="middle" font-size="22">Mature</text>
    </g>

    <!-- leader dots -->
    <g class="leaders" fill="var(--ink)">
      <circle cx="355" cy="354" r="3"/><circle cx="368" cy="354" r="3"/><circle cx="381" cy="354" r="3"/>
      <circle cx="355" cy="632" r="3"/><circle cx="368" cy="632" r="3"/><circle cx="381" cy="632" r="3"/>
      <circle cx="853" cy="354" r="3"/><circle cx="866" cy="354" r="3"/><circle cx="879" cy="354" r="3"/>
      <circle cx="853" cy="632" r="3"/><circle cx="866" cy="632" r="3"/><circle cx="879" cy="632" r="3"/>
    </g>

    <!-- vertical rules -->
    <g class="rules">
      <rect x="344" y="290" width="2" height="128" fill="url(#rule-purple)"/>
      <rect x="344" y="568" width="2" height="129" fill="url(#rule-green)"/>
      <rect x="889" y="290" width="2" height="128" fill="url(#rule-blue)"/>
      <rect x="889" y="568" width="2" height="129" fill="url(#rule-red)"/>
    </g>

    <!-- stage descriptions -->
    <g class="stage-label">
      <text x="336" y="346" text-anchor="end">The Enthusiastic Christian School</text>
      <text x="336" y="377" text-anchor="end">0-10 Years</text>
      <text x="335" y="623" text-anchor="end">The Confident Christian School</text>
      <text x="335" y="652" text-anchor="end">10-15 Years</text>
      <text x="898" y="346">The Proud Christian School</text>
      <text x="900" y="377">20+ Years</text>
      <text x="900" y="623">The Inspired Christian School</text>
      <text x="900" y="652">15-30+ Years</text>
    </g>
  </svg>

  <p class="copyright">© 2020 Harbor Academy Advisors.</p>
</div>
</body>
</html>
```